Corvelle Vintners LLC Website

We need a website design for a winery. Our consumer target market will be a millennial demographic, hip, fresh, and upscale.
High end impact images, interactive pages, e-commerce, etc...
The following are examples of what we would be looking to accomplish:

http://www.pebbleridgecellars.example/
482estate.example
http://www.grapelarkstudio.example/portfolio/

There is no tasting room, all sales are via wine club and internet sales.

Target Market(s)

Millennials are the generation born between 1982 and sometime in the early 2000’s. However, these boundaries aren’t set in stone. Usually highly educated professionals with disposable income.

```html
<!DOCTYPE html>
<html lang="en">
<head>
<meta charset="utf-8">
<title>Corvelle Vintners</title>
<link href="https://fonts.googleapis.com/css2?family=Cinzel:wght@400;700&family=Open+Sans:wght@400;600&display=swap" rel="stylesheet">
<style>
:root{
  --wine:#a8173f;
  --wine-dark:#7e0f2e;
  --ink:#2b2b2b;
  --text:#6d6d6d;
  --nav:#2a2a2a;
  --band:#efefef;
  --footer:#232323;
  --footer-deep:#1a1a1a;
  --line:#dcdcdc;
  --white:#ffffff;
}
*{box-sizing:border-box;margin:0;padding:0}
html,body{width:1200px;height:2252px;overflow:hidden;background:var(--white)}
body{position:relative;font-family:"Open Sans",Arial,sans-serif;color:var(--text)}
.abs{position:absolute}
.serif{font-family:"Cinzel",Georgia,serif}

/* header */
.brand{left:40px;top:60px;width:260px;text-align:center;color:var(--wine);font-family:"Cinzel",Georgia,serif;font-weight:700;font-size:26px;line-height:32px;letter-spacing:1px}
.phone{left:730px;top:52px;display:flex;align-items:center;gap:10px;color:var(--ink);font-size:16px;font-weight:600}
.phone .dot{width:30px;height:30px;border-radius:50%;background:var(--wine);display:flex;align-items:center;justify-content:center}
.search{left:978px;top:48px;width:190px;height:36px;border:1px solid var(--line);display:flex}
.search span{flex:1;font-size:12px;color:#9a9a9a;padding:10px 10px}
.search b{width:36px;background:var(--wine);display:flex;align-items:center;justify-content:center}

.nav{left:0;top:146px;width:1200px;height:40px;background:var(--nav);display:flex;padding-left:120px}
.nav a{color:#e6e6e6;font-size:12px;font-weight:600;letter-spacing:.5px;text-decoration:none;height:40px;line-height:40px;padding:0 24px}
.nav a.active{background:var(--wine);color:var(--white)}

/* hero */
.hero{left:0;top:186px;width:1200px;height:334px;background:radial-gradient(ellipse at 20% 30%,#5a2a3e 0%,#2c1820 45%,#140c0e 100%),#1a1012}
.hero-bottle{left:880px;top:186px;width:220px;height:334px;background:radial-gradient(ellipse at 50% 60%,rgba(140,100,60,.55),rgba(0,0,0,0) 70%)}
.hero-title{left:140px;top:280px;width:420px;text-align:center;color:var(--white);font-family:"Cinzel",Georgia,serif;font-size:34px;font-weight:700}
.hero-sub{left:150px;top:330px;width:400px;text-align:center;color:#e2d6d9;font-size:13px;line-height:19px}
.btn{display:inline-block;background:var(--wine);color:var(--white);font-size:13px;text-align:center}
.hero-btn{left:295px;top:378px;width:110px;height:34px;line-height:34px}

/* welcome */
.section-title{width:1200px;left:0;text-align:center;font-family:"Cinzel",Georgia,serif;font-weight:700;color:var(--ink);font-size:32px}
.rule{width:60px;height:2px;background:var(--wine);left:570px}
.welcome-text{left:140px;top:640px;width:920px;text-align:center;font-size:14px;line-height:22px}

.card{top:880px;width:300px;height:320px;background:var(--white);box-shadow:0 2px 10px rgba(0,0,0,.12);text-align:center}
.card .icon{position:absolute;left:95px;top:-55px;width:110px;height:110px;border-radius:50%;background:var(--white);border:1px solid var(--line);display:flex;align-items:center;justify-content:center;box-shadow:0 2px 6px rgba(0,0,0,.08)}
.card h3{position:absolute;left:0;top:112px;width:300px;font-family:"Cinzel",Georgia,serif;font-size:22px;color:var(--ink);font-weight:400}
.card .mini{position:absolute;left:130px;top:148px;width:40px;height:2px;background:var(--wine)}
.card p{position:absolute;left:30px;top:164px;width:240px;font-size:13px;line-height:20px}
.card .more{position:absolute;left:95px;top:252px;width:110px;height:34px;line-height:32px;border:1px solid var(--wine);color:var(--wine);font-size:13px}

/* products */
.band{left:0;top:1340px;width:1200px;height:500px;background:var(--band)}
.product{top:1432px;width:200px;height:330px;background:var(--white);box-shadow:0 1px 4px rgba(0,0,0,.1);overflow:hidden}
.product .shot{position:absolute;left:10px;top:10px;width:180px;height:180px;background:#f6f6f6;display:flex;justify-content:center;align-items:flex-end;padding-bottom:10px}
.bottle{width:34px;height:150px;border-radius:14px 14px 4px 4px}
.product .ribbon{position:absolute;right:0;top:0;width:0;height:0;border-top:56px solid var(--wine);border-left:56px solid transparent}
.product .ribbon-text{position:absolute;right:4px;top:12px;transform:rotate(45deg);color:var(--white);font-size:10px;font-weight:600}
.product .name{position:absolute;left:0;top:210px;width:200px;text-align:center;font-size:12px;color:var(--ink);font-weight:600}
.product .price{position:absolute;left:0;top:236px;width:200px;text-align:center;font-size:14px;color:var(--wine);font-weight:600}
.product .qty{position:absolute;left:22px;top:274px;width:60px;height:28px;border:1px solid var(--line);font-size:12px;line-height:26px;text-align:center;color:var(--ink)}
.product .add{position:absolute;left:112px;top:274px;width:68px;height:28px;border:1px solid var(--wine);color:var(--wine);font-size:12px;line-height:26px;text-align:center}

/* footer */
.footer{left:0;top:1848px;width:1200px;height:404px;background:var(--footer)}
.foot-brand{left:110px;top:1960px;width:220px;text-align:center;color:var(--white);font-family:"Cinzel",Georgia,serif;font-weight:700;font-size:24px;line-height:30px;letter-spacing:1px}
.col-title{font-family:"Cinzel",Georgia,serif;color:var(--white);font-size:17px;font-weight:700}
.menu{left:382px;top:1958px;list-style:none}
.menu li{font-size:12px;color:#bdbdbd;line-height:18px}
.menu li::before{content:"› ";color:var(--wine)}
.contact-row{display:flex;align-items:flex-start;gap:10px;font-size:12px;color:#bdbdbd;line-height:18px}
.contact-row i{flex:0 0 18px;height:18px;border-radius:50%;background:var(--wine);display:flex;align-items:center;justify-content:center}
.field{left:830px;width:270px;height:28px;border:1px solid #444;background:#2c2c2c;font-size:11px;color:#8a8a8a;padding:6px 8px}
.submit{left:1030px;top:2144px;width:70px;height:26px;line-height:26px;font-size:12px}
.bottom{left:0;top:2196px;width:1200px;height:56px;background:var(--footer-deep)}
.copy{left:40px;top:2216px;font-size:11px;color:#8a8a8a}
.social{top:2211px;width:26px;height:26px;border-radius:50%;background:#3a3a3a}
</style>
</head>
<body>

<header>
  <div class="abs brand">Corvelle<br>Vintners</div>
  <div class="abs phone">
    <span class="dot"><svg width="14" height="14" viewBox="0 0 24 24"><path fill="#fff" d="M6.6 10.8a15 15 0 0 0 6.6 6.6l2.2-2.2c.3-.3.7-.4 1-.2 1.1.4 2.3.6 3.6.6.6 0 1 .4 1 1V20c0 .6-.4 1-1 1A17 17 0 0 1 3 4c0-.6.4-1 1-1h3.5c.6 0 1 .4 1 1 0 1.3.2 2.5.6 3.6.1.3 0 .7-.2 1z"/></svg></span>
    +61 400 555 218
  </div>
  <div class="abs search"><span>Search your keywords...</span><b><svg width="14" height="14" viewBox="0 0 24 24"><circle cx="10" cy="10" r="6" fill="none" stroke="#fff" stroke-width="2.5"/><path d="M15 15l6 6" stroke="#fff" stroke-width="2.5"/></svg></b></div>
  <nav class="abs nav">
    <a class="active">HOME</a><a>WINE</a><a>CONTACT US</a><a>EVENTS</a><a>GALLERY</a><a>ABOUT US</a><a>CART</a><a>AWARDS</a><a>MEMBERS</a>
  </nav>
</header>

<section>
  <div class="abs hero" role="img" aria-label="Dark cellar photograph with grape clusters on the left and a bottle of red wine with a glass on a barrel at the right"></div>
  <div class="abs hero-bottle"></div>
  <h1 class="abs hero-title">Corvelle Vintners</h1>
  <p class="abs hero-sub">A fine vintage is a quiet pleasure, shared slowly with the people you love most.</p>
  <span class="abs btn hero-btn">View more</span>
</section>

<section>
  <h2 class="abs section-title" style="top:584px">Welcome to Corvelle Vintners</h2>
  <div class="abs rule" style="top:628px"></div>
  <p class="abs welcome-text">Small-batch wines from cool-climate vineyards, crafted for the table and delivered straight to your door through our wine club and online cellar. Every bottle is made in limited runs, so when a vintage is gone, it is gone.</p>

  <div class="abs card" style="left:90px">
    <div class="icon"><svg width="44" height="44" viewBox="0 0 24 24"><path fill="#a8173f" d="M3 5l6-2 6 2 6-2v16l-6 2-6-2-6 2zM9 4.5v14.8M15 6.5v14.8" stroke="#fff" stroke-width="1"/></svg></div>
    <h3>TOUR</h3><div class="mini"></div>
    <p>Walk the rows with our winemakers on a private vineyard tour and taste current releases beside the barrels where they rested.</p>
    <span class="more">View more</span>
  </div>
  <div class="abs card" style="left:450px">
    <div class="icon"><svg width="48" height="40" viewBox="0 0 26 20"><path fill="#a8173f" d="M1 3h15v11H1zM16 7h5l4 4v3h-9z"/><circle cx="6" cy="16" r="2.6" fill="#a8173f" stroke="#fff" stroke-width="1"/><circle cx="20" cy="16" r="2.6" fill="#a8173f" stroke="#fff" stroke-width="1"/></svg></div>
    <h3>FREE SHIPPING</h3><div class="mini"></div>
    <p>Every order over two bottles ships free, packed carefully and tracked from our cellar door all the way to yours.</p>
    <span class="more">View more</span>
  </div>
  <div class="abs card" style="left:810px">
    <div class="icon"><svg width="42" height="42" viewBox="0 0 24 24"><rect x="3" y="5" width="18" height="16" rx="1.5" fill="#a8173f"/><path d="M7 3v4M17 3v4" stroke="#a8173f" stroke-width="2"/><g fill="#fff"><rect x="6" y="10" width="3" height="3"/><rect x="10.5" y="10" width="3" height="3"/><rect x="15" y="10" width="3" height="3"/><rect x="6" y="15" width="3" height="3"/><rect x="10.5" y="15" width="3" height="3"/><rect x="15" y="15" width="3" height="3"/></g></svg></div>
    <h3>EVENTS</h3><div class="mini"></div>
    <p>Join seasonal dinners, release parties and club evenings where new vintages are poured first for our members.</p>
    <span class="more">View more</span>
  </div>
</section>

<section>
  <div class="abs band"></div>
  <h2 class="abs section-title" style="top:1360px">Our Products</h2>
  <div class="abs rule" style="top:1404px"></div>

  <div class="abs product" style="left:144px">
    <div class="shot"><div class="bottle" role="img" aria-label="Bottle of red wine" style="background:linear-gradient(90deg,#1c1214,#4a2a30,#1c1214)"></div></div>
    <div class="ribbon"></div><span class="ribbon-text">NEW</span>
    <div class="name">SHIRAZ 2012</div>
    <div class="price">$18.10</div>
    <div class="qty">1</div><div class="add">Add cart</div>
  </div>
  <div class="abs product" style="left:366px">
    <div class="shot"><div class="bottle" role="img" aria-label="Bottle of rosé wine" style="background:linear-gradient(90deg,#c9606a,#f0a4a0,#c9606a)"></div></div>
    <div class="name">RIESLING 2013</div>
    <div class="price">$18.10</div>
    <div class="qty">1</div><div class="add">Add cart</div>
  </div>
  <div class="abs product" style="left:588px">
    <div class="shot"><div class="bottle" role="img" aria-label="Bottle of white wine in green glass" style="background:linear-gradient(90deg,#6f7a34,#c8cf7a,#6f7a34)"></div></div>
    <div class="name">SAUVIGNON BLANC 2014</div>
    <div class="price">$18.10</div>
    <div class="qty">1</div><div class="add">Add cart</div>
  </div>
  <div class="abs product" style="left:810px">
    <div class="shot"><div class="bottle" role="img" aria-label="Bottle of golden white wine" style="background:linear-gradient(90deg,#b87b22,#f0c66a,#b87b22)"></div></div>
    <div class="name">SAUVIGNON BLANC 2015</div>
    <div class="price">$18.10</div>
    <div class="qty">1</div><div class="add">Add cart</div>
  </div>
</section>

<footer>
  <div class="abs footer"></div>
  <div class="abs foot-brand">Corvelle<br>Vintners</div>

  <div class="abs col-title" style="left:382px;top:1926px">Menu</div>
  <ul class="abs menu">
    <li>Home</li><li>Wine</li><li>Contact us</li><li>Events</li><li>Gallery</li><li>About us</li><li>Cart</li><li>Members</li><li>Awards</li>
  </ul>

  <div class="abs col-title" style="left:560px;top:1926px">Contact Us</div>
  <div class="abs contact-row" style="left:560px;top:1962px;width:220px">
    <i><svg width="10" height="10" viewBox="0 0 24 24"><path fill="#fff" d="M12 2a7 7 0 0 0-7 7c0 5 7 13 7 13s7-8 7-13a7 7 0 0 0-7-7zm0 9.5A2.5 2.5 0 1 1 12 6.5a2.5 2.5 0 0 1 0 5z"/></svg></i>
    <span>12 Harbour Lane,<br>NSW 2000 Australia</span>
  </div>
  <div class="abs contact-row" style="left:560px;top:2010px">
    <i><svg width="10" height="10" viewBox="0 0 24 24"><path fill="#fff" d="M2 5h20v14H2zm2 2v.5l8 5 8-5V7z"/></svg></i>
    <span>hello@corvellevintners.example</span>
  </div>
  <div class="abs contact-row" style="left:560px;top:2040px">
    <i><svg width="10" height="10" viewBox="0 0 24 24"><path fill="#fff" d="M6.6 10.8a15 15 0 0 0 6.6 6.6l2.2-2.2c.3-.3.7-.4 1-.2 1.1.4 2.3.6 3.6.6.6 0 1 .4 1 1V20c0 .6-.4 1-1 1A17 17 0 0 1 3 4c0-.6.4-1 1-1h3.5c.6 0 1 .4 1 1 0 1.3.2 2.5.6 3.6.1.3 0 .7-.2 1z"/></svg></i>
    <span>+61 400 555 218</span>
  </div>

  <div class="abs col-title" style="left:830px;top:1926px">Quick Contact</div>
  <div class="abs field" style="top:1962px">Enter your name...</div>
  <div class="abs field" style="top:1998px">E-mail address...</div>
  <div class="abs field" style="top:2034px;height:100px">Message...</div>
  <span class="abs btn submit">Submit</span>

  <div class="abs bottom"></div>
  <div class="abs copy">Copyright 2015 © All Rights Reserved</div>
  <span class="abs social" style="left:1010px;background:var(--wine)"></span>
  <span class="abs social" style="left:1042px"></span>
  <span class="abs social" style="left:1074px;background:var(--wine)"></span>
  <span class="abs social" style="left:1106px"></span>
  <svg class="abs" style="left:1144px;top:2216px" width="16" height="16" viewBox="0 0 16 16"><path d="M8 3l5 6H3z" fill="#8a8a8a"/></svg>
</footer>

</body>
</html>
```